Next-Gen B2B Sales Negotiation App - UI Design for iOS

Develop a user-friendly dark-mode interface for a B2B sales negotiation assistant app for a company called Quorvel. The UI will showcase a single screen with features like counterparty search, agenda selection, and email drafting. Design should reflect a functional iOS app with realistic placeholder data to create a genuine experience.

Precise task description in attachment.

Target Market(s)

B2B

Requirements
Must have
• Each UI picture should look like a screen capture of an iphone
Nice to have
• The UI designs need to show the navigation and the app in use

```html
<!DOCTYPE html>
<html lang="en">
<head>
<meta charset="utf-8">
<title>Quorvel – Sales Negotiation App Screens</title>
<link href="https://fonts.googleapis.com/css2?family=Exo+2:wght@500&family=Poppins:wght@400;500;600&family=Silkscreen:wght@400;700&display=swap" rel="stylesheet">
<style>
:root{
  --page:#ffffff;
  --screen:#1b0d20;
  --screen-deep:#140a18;
  --ink:#ffffff;
  --pink:#ff4499;
  --pink-soft:#f5a3c6;
  --cyan:#44dcf5;
  --teal:#26a0a8;
  --mail-blue:#5aa0f5;
  --net-blue:#1565c8;
  --call-green:#22b810;
  --panel:#3a2f40;
  --panel-inner:#4a3f50;
  --form-panel:#2e2434;
  --card-frame:#22303e;
}
*{margin:0;padding:0;box-sizing:border-box}
html,body{width:1200px;height:583px;overflow:hidden;background:var(--page)}
.stage{width:1960px;height:960px;transform:scale(0.6122,0.6073);transform-origin:0 0;position:relative;font-family:"Poppins",sans-serif}
.screen{position:absolute;top:78px;width:414px;height:800px;overflow:hidden;
  background:radial-gradient(ellipse at 50% 30%,#24112b 0%,var(--screen) 55%,var(--screen-deep) 100%);color:var(--ink)}
.screen > *{position:absolute}
.brand{left:0;width:414px;top:18px;text-align:center;font-family:"Exo 2",sans-serif;font-weight:500;font-size:38px;letter-spacing:1px}
.menu{left:370px;top:32px;width:24px;height:18px}
.pixel{font-family:"Silkscreen",sans-serif;font-weight:700;letter-spacing:1px;white-space:nowrap}
.audience-icon{width:68px;height:68px;border-radius:50%;top:96px;box-shadow:-8px -8px 0 6px rgba(255,68,153,.18)}
.audience-label{top:182px;width:140px;text-align:center;font-size:13px}
.divider{left:0;width:414px;height:8px}
.agenda-tile{left:64px;top:310px;width:286px;height:80px;background:#fff;border-radius:6px}
.agenda-tile span{position:absolute;left:12px;top:10px;width:262px;height:60px;border:2px solid var(--pink);border-radius:8px;background:#fff2f8;color:#111;display:flex;align-items:center;justify-content:center;font-size:34px;letter-spacing:5px}
.panel{background:var(--panel);border-radius:8px}
.panel-inner{background:var(--panel-inner);border-radius:6px}
.btn{display:flex;align-items:center;justify-content:center;gap:14px;color:#fff;font-weight:600;font-size:14px;border-radius:3px}
.btn svg{width:22px;height:18px}
.card-frame{left:41px;top:215px;width:332px;height:265px;background:var(--card-frame);border-radius:20px}
.card-white{left:53px;top:231px;width:308px;height:234px;background:#fff;border-radius:20px}
.pill{left:80px;width:255px;height:42px;border-radius:6px;color:#fff;font-weight:600;font-size:14px;display:flex;align-items:center;justify-content:center}
.band{left:0;top:556px;width:414px;height:19px}
.ghost{background:#2a1f30;border-radius:18px}
.ghost-btn{left:80px;width:255px;height:42px;background:#1f1a28;border-radius:6px;color:#2e2a3a;font-weight:600;font-size:14px;display:flex;align-items:center;justify-content:center}
.message{left:80px;top:86px;width:257px;height:294px;background:var(--pink);text-align:center}
.message h2{margin-top:20px;font-size:22px;font-weight:600}
.message p{margin-top:10px;font-size:12px;line-height:26px}
.send{left:60px;top:225px;width:138px;height:34px;background:#fff;color:var(--pink);display:flex;align-items:center;justify-content:center;font-size:13px}
.form-panel{left:20px;top:103px;width:374px;height:287px;background:var(--form-panel);border-radius:8px}
.form-label{left:36px;font-size:16px;line-height:27px}
.field{left:192px;width:186px;height:31px;border:1px solid #ddd;border-radius:2px}
.field svg{position:absolute;right:8px;top:9px;width:12px;height:12px}
.check{top:272px;font-size:13px;display:flex;align-items:center;gap:8px}
.check i{width:13px;height:13px;border:1px solid #ccc;display:inline-block;position:relative}
.submit{left:116px;top:313px;width:182px;height:36px;background:var(--pink);display:flex;align-items:center;justify-content:center;font-size:13px}
.benefit-icon{left:20px;width:57px;height:57px;border-radius:50%;border:1.5px solid #ddd;background:radial-gradient(circle,#3a2c42 0 40%,transparent 42%)}
.benefit{left:98px;font-size:15px;line-height:30px;letter-spacing:1.5px}
</style>
</head>
<body>
<div class="stage">

  <!-- Screen 1: audience + contact channels -->
  <section class="screen" style="left:65px">
    <div class="brand">quorvel</div>
    <svg class="menu" viewBox="0 0 24 18" stroke="#fff" stroke-width="2"><path d="M2 2h22M8 9h16M4 16h20"/></svg>
    <div class="audience-icon" role="img" aria-label="Company icon" style="left:39px;background:var(--pink)"></div>
    <div class="audience-icon" role="img" aria-label="Individuals icon" style="left:177px;background:var(--cyan);box-shadow:-8px -8px 0 6px rgba(68,220,245,.18)"></div>
    <div class="audience-icon" role="img" aria-label="Group icon" style="left:317px;background:var(--pink)"></div>
    <div class="audience-label pixel" style="left:3px">Company</div>
    <div class="audience-label pixel" style="left:141px">Individuals</div>
    <div class="audience-label pixel" style="left:276px">Group</div>
    <svg class="divider" style="top:254px" viewBox="0 0 414 8"><rect width="207" height="6" y="1" fill="#ff4499"/><rect x="213" width="7" height="7" fill="#f5a3c6"/><rect x="226" width="7" height="7" fill="#f5a3c6"/><rect x="239" width="7" height="7" fill="#26a0a8"/><rect x="252" width="7" height="7" fill="#44dcf5"/><rect x="263" width="151" height="6" y="1" fill="#44dcf5"/></svg>
    <div class="agenda-tile"><span class="pixel">Agenda</span></div>
    <svg class="divider" style="top:440px" viewBox="0 0 414 8"><rect width="207" height="6" y="1" fill="#ff4499"/><rect x="213" width="7" height="7" fill="#f5a3c6"/><rect x="226" width="7" height="7" fill="#f5a3c6"/><rect x="239" width="7" height="7" fill="#26a0a8"/><rect x="252" width="7" height="7" fill="#44dcf5"/><rect x="263" width="151" height="6" y="1" fill="#44dcf5"/></svg>
    <div class="panel" style="left:54px;top:503px;width:307px;height:237px"></div>
    <div class="panel-inner" style="left:74px;top:520px;width:266px;height:204px"></div>
    <div class="btn" style="left:93px;top:548px;width:228px;height:36px;background:var(--mail-blue)">EMAIL <svg viewBox="0 0 22 16" fill="none" stroke="#fff" stroke-width="1.5"><rect x="1" y="1" width="20" height="14"/><path d="M1 1l10 8 10-8"/></svg></div>
    <div class="btn" style="left:91px;top:603px;width:228px;height:35px;background:var(--net-blue)">PRONET MESSAGE <svg viewBox="0 0 18 18" style="width:12px;height:12px"><rect width="18" height="18" fill="#fff"/></svg></div>
    <div class="btn" style="left:93px;top:658px;width:228px;height:36px;background:var(--call-green)">PHONE CALL <svg viewBox="0 0 24 24" fill="none" stroke="#fff" stroke-width="1.6"><path d="M5 3l4 1 1 4-2 2a12 12 0 0 0 6 6l2-2 4 1 1 4-2 2C10 21 3 14 3 5z"/><path d="M14 3a7 7 0 0 1 7 7M14 7a3 3 0 0 1 3 3"/></svg></div>
  </section>

  <!-- Screen 2: agenda selection -->
  <section class="screen" style="left:536px">
    <div class="brand">quorvel</div>
    <svg class="menu" viewBox="0 0 24 18" stroke="#fff" stroke-width="2"><path d="M2 2h22M8 9h16M4 16h20"/></svg>
    <div class="card-frame"></div>
    <div class="card-white"></div>
    <div class="pill" style="top:263px;background:var(--pink)">COMPANY BRINDLE CO CEO</div>
    <div class="pill" style="top:323px;background:var(--cyan)">AGENDA</div>
    <div class="pill" style="top:383px;background:var(--teal)">METHOD EMAIL</div>
    <svg class="band" viewBox="0 0 414 19"><rect width="167" height="19" fill="#ff4499"/><rect x="178" width="19" height="19" fill="#f5a3c6"/><rect x="208" width="19" height="19" fill="#fde0ec"/><rect x="238" width="19" height="19" fill="#26a0a8"/><rect x="268" width="19" height="19" fill="#2bb8c4"/><rect x="298" width="116" height="19" fill="#44dcf5"/></svg>
  </section>

  <!-- Screen 3: drafted email -->
  <section class="screen" style="left:1008px">
    <div class="brand">quorvel</div>
    <svg class="menu" viewBox="0 0 24 18" stroke="#fff" stroke-width="2"><path d="M2 2h22M8 9h16M4 16h20"/></svg>
    <div class="ghost" style="left:42px;top:258px;width:330px;height:262px;background:#1f1626"></div>
    <div class="ghost" style="left:53px;top:270px;width:308px;height:235px"></div>
    <div class="ghost-btn" style="top:363px">AGENDA</div>
    <div class="ghost-btn" style="top:423px">COMPANY BRINDLE CO CEO</div>
    <article class="message">
      <h2>Hi Marek</h2>
      <p>I am reaching out<br>to you as I have a solution to save your<br>money and time. I am kindly proposing<br>a meeting for week 8, for instance on<br>Monday 17 February. Best regards,<br>Ilkka”</p>
      <div class="send pixel" style="position:absolute">Send now</div>
    </article>
    <svg class="band" viewBox="0 0 414 19"><rect width="167" height="19" fill="#3a1630"/><rect x="178" width="19" height="19" fill="#3a2030"/><rect x="208" width="19" height="19" fill="#3a2030"/><rect x="238" width="19" height="19" fill="#1a2c36"/><rect x="268" width="19" height="19" fill="#1a2c36"/><rect x="298" width="116" height="19" fill="#1a2c36"/></svg>
  </section>

  <!-- Screen 4: meeting scheduling -->
  <section class="screen" style="left:1479px">
    <div class="brand">quorvel</div>
    <svg class="menu" viewBox="0 0 24 18" stroke="#fff" stroke-width="2"><path d="M2 2h22M8 9h16M4 16h20"/></svg>
    <div class="form-panel"></div>
    <div class="form-label" style="top:143px">Meeting Duration</div>
    <div class="field" style="top:144px"><svg viewBox="0 0 12 12" fill="none" stroke="#fff" stroke-width="2"><path d="M2 4l4 4 4-4"/></svg></div>
    <div class="form-label" style="top:196px">When Meeting<br>choose date</div>
    <div class="field" style="top:214px"><svg viewBox="0 0 12 12" fill="#fff"><rect x="1" y="2" width="10" height="9"/></svg></div>
    <div class="check" style="left:132px"><i><svg viewBox="0 0 13 13" style="position:absolute;left:1px;top:-1px;width:12px;height:12px" fill="none" stroke="#fff" stroke-width="2"><path d="M2 6l3 3 6-7"/></svg></i>Online</div>
    <div class="check" style="left:212px"><i></i>On-Site</div>
    <div class="submit pixel">Submit</div>
    <div class="benefit-icon" role="img" aria-label="Money bag icon" style="top:444px"></div>
    <div class="benefit pixel" style="top:442px">We can make you more<br>money</div>
    <div class="benefit-icon" role="img" aria-label="Clock icon" style="top:534px"></div>
    <div class="benefit pixel" style="top:547px">We can save your time</div>
  </section>

</div>
</body>
</html>
```